Storm postcards

We need postcards for our roofing company. A recent storm hit our area and we are looking to market to those that were hit in the area. We want something that is simple, but flashy enough to get peoples attention. We are looking for something that has a good blend of flash and professional look.

Name of the company is Tolvey Building Partners LLC

Target Market(s)

Homeowners

Font styles to use
Serif

Requirements
Must have
• Phone number 480-913-2748, The storm was mostly a wind storm, some of the postcards attached are for hail but this one should focus of STORM DAMAGE.
• My business license number has to be on the postcard somewhere preferably small and hidden ROC #284063

```html
<!DOCTYPE html>
<html lang="en">
<head>
<meta charset="utf-8">
<title>Tolvey Building Partners – Storm Damage Postcard</title>
<link rel="stylesheet" href="https://fonts.googleapis.com/css2?family=Bebas+Neue&family=Roboto+Condensed:wght@400;700&display=swap">
<style>
  :root {
    --red: #e32127;
    --blue: #0d93d8;
    --blue-deep: #0b7fb0;
    --charcoal: #242729;
    --panel: #2b2e31;
    --white: #ffffff;
    --muted: #8a8f94;
    --sky-top: #f4f6f8;
    --sky-mid: #b9c6d2;
    --roof-grey: #8d949b;
  }
  * { margin: 0; padding: 0; box-sizing: border-box; }
  html, body { width: 1200px; height: 953px; overflow: hidden; background: #d9dadc; }
  .postcard { position: relative; width: 1200px; height: 953px; background: var(--white); overflow: hidden; }
  .shapes { position: absolute; inset: 0; }
  .hero-photo { position: absolute; left: 0; top: 110px; width: 980px; height: 652px;
    background: linear-gradient(180deg, var(--sky-top) 0%, var(--sky-mid) 30%, #a7b0b8 55%, var(--roof-grey) 80%, #6f767c 100%); }
  .brand { position: absolute; left: 58px; top: 66px; display: flex; align-items: center; gap: 12px; }
  .brand-mark { width: 36px; height: 36px; background: var(--red); }
  .brand-name { font-family: "Roboto Condensed", sans-serif; font-weight: 700; font-size: 34px; color: var(--blue); letter-spacing: 1px; text-transform: uppercase; }
  .headline { position: absolute; left: 58px; top: 136px; font-family: "Bebas Neue", sans-serif; font-weight: 400; font-size: 116px; line-height: 99px;
    color: var(--red); white-space: nowrap; transform: scaleX(0.74); transform-origin: left top;
    text-shadow: 4px 5px 0 rgba(0,0,0,0.55); }
  .offer-bubble { position: absolute; left: 874px; top: 238px; width: 266px; height: 246px; }
  .offer-text { position: absolute; left: 827px; top: 268px; width: 360px; font-family: "Bebas Neue", sans-serif; font-size: 84px; line-height: 70px;
    color: var(--white); text-align: center; }
  .offer-text span { display: inline-block; white-space: nowrap; transform: scaleX(0.64); transform-origin: center; }
  .offer-text .offer-line-top { letter-spacing: 4px; }
  .callout { position: absolute; right: 61px; top: 508px; text-align: right; font-family: "Roboto Condensed", sans-serif; font-weight: 700;
    color: var(--white); font-size: 41px; line-height: 56px; }
  .callout .emphasis { display: block; font-family: "Bebas Neue", sans-serif; font-weight: 400; color: var(--red); font-size: 102px; line-height: 84px;
    transform: scaleX(0.76); transform-origin: right center; white-space: nowrap; margin: 2px 0 -4px; }
  .contact { position: absolute; left: 70px; top: 790px; font-family: "Roboto Condensed", sans-serif; font-weight: 700; color: var(--red); }
  .contact-row { display: flex; align-items: center; gap: 18px; }
  .contact-address { font-size: 31px; }
  .contact-phone { font-size: 56px; margin-top: 6px; }
  .contact svg { fill: var(--red); flex: none; }
  .licence { position: absolute; left: 70px; top: 920px; font-family: "Roboto Condensed", sans-serif; font-weight: 400; font-size: 14px;
    color: var(--muted); letter-spacing: 0.5px; }
</style>
</head>
<body>
<main class="postcard">
  <div class="hero-photo" role="img" aria-label="Photo of a house with storm-damaged shingle roof against a cloudy sky"></div>

  <svg class="shapes" width="1200" height="953" viewBox="0 0 1200 953" aria-hidden="true">
    <rect class="footer-band" x="0" y="762" width="1200" height="191" fill="var(--charcoal)"/>
    <polygon class="side-panel" points="978,0 1200,0 1200,953 902,953 777,681 654,681" fill="var(--panel)"/>
    <polygon class="accent-stripe" points="941,0 978,0 654,681 616,681" fill="var(--blue)"/>
    <polygon class="accent-fold" points="616,681 777,681 694,830" fill="var(--blue-deep)"/>
    <polygon class="accent-triangle" points="639,953 780,681 902,953" fill="var(--blue)"/>
  </svg>

  <div class="brand">
    <span class="brand-mark"></span>
    <span class="brand-name">Tolvey Building Partners</span>
  </div>

  <h1 class="headline">Did your roof get damaged<br>by the recent storm?</h1>

  <svg class="offer-bubble" viewBox="0 0 266 246" aria-hidden="true">
    <path d="M4 52 L226 4 L262 26 L262 202 L250 202 L262 244 L212 202 L4 202 Z" fill="var(--white)"/>
    <path d="M12 58 L222 14 L254 30 L254 194 L12 194 Z" fill="var(--red)"/>
    <path d="M222 14 L254 30 L232 34 Z" fill="#f3d6d6"/>
  </svg>
  <p class="offer-text"><span class="offer-line-top">Free Roof</span><br><span>Inspection</span></p>

  <p class="callout">If your<span class="emphasis">Concerned</span>about your roof<br>please give us<br>a call now!</p>

  <div class="contact">
    <div class="contact-row contact-address">
      <svg width="26" height="36" viewBox="0 0 24 34" aria-hidden="true"><path d="M12 0C5.4 0 0 5.4 0 12c0 9 12 22 12 22s12-13 12-22C24 5.4 18.6 0 12 0zm0 17a5 5 0 1 1 0-10 5 5 0 0 1 0 10z"/></svg>
      <span>418 Elm, Mesa, Arizona</span>
    </div>
    <div class="contact-row contact-phone">
      <svg width="40" height="40" viewBox="0 0 24 24" aria-hidden="true"><path d="M6.6 10.8a15.1 15.1 0 0 0 6.6 6.6l2.2-2.2c.3-.3.7-.4 1-.2 1.1.4 2.3.6 3.6.6.6 0 1 .4 1 1V20c0 .6-.4 1-1 1A17 17 0 0 1 3 4c0-.6.4-1 1-1h3.5c.6 0 1 .4 1 1 0 1.2.2 2.4.6 3.6.1.3 0 .7-.2 1z"/></svg>
      <span>480-913-2748</span>
    </div>
  </div>

  <p class="licence">ROC #284063</p>
</main>
</body>
</html>
```